Piano genealogy graphs template, for a large poster printing

Hello and thank you for your interest in my project.
I need a poster template, so I can create structures similar to the one I have uploaded. I want to completely replace or improve my poor previous design which is attached.
I need to be able to input names and dates into boxes of various colors, arrows pointing between boxes. I would also like to be able to label each graph (not each box).
I am looking at something that would be legible when printed, in a one consistent professional layout of 2A0 (around 1189x1682 mm) poster (I know it is large). The design template required here can include just few sample text boxes with sample flags on a suitable background, for me to multiply later and spread across the whole poster.
The positioning of the boxes is not important.
Please let me know if more clarification is required.
Thank you for your help.

Feel free to follow what I have attached in the file, or change the design completely.

UPDATE 4/12: I have uploaded two more graphs as an example. At this stage of the contest, I would like to have one of those graphs done, and I am planning to offer a 'freelance job' to one or two designers, who will be willing to do the whole 10 graphs on one poster.
Updates

Reason: Dear Designers, Since the project is rather complex and large-scale, I have decided to give everyone more time to work on their designs. I will consider extending it further if any of you require additional time. Best wishes, bronisław

Dear Designers, I would like to inform you that the contest for my poster is now closed and that I have assigned the prizes. I would like to thank all of you for submiting your high-quality designs, and for your participation. It was a great pleasure working with all of you. Due to the large size of the project itself (large number of graphs to be fitted on a single poster), I had to focus on providing feedback to only those designers who provided projects closest to what I was expecting at the early stages of the contest. I wish you all the best for the future, Kind regards, Bronisław

Target Market(s)

Pianists, historians

Industry/Entity Type

Printing

Requirements
Must have
• Consistent design, but allow to clearly delineate various genealogy trees.

```html
<!DOCTYPE html>
<html lang="en">
<head>
<meta charset="utf-8">
<title>Pianist Genealogy Poster</title>
<link rel="stylesheet" href="https://fonts.googleapis.com/css2?family=Pathway+Gothic+One&display=swap">
<style>
  :root {
    --bg: #0b0b0b;
    --text: #e6e6e6;
    --connector: #8c8c8c;
    --flourish: #4a4a4a;
    --it-green: #138a3e;
    --it-white: #f4f4f4;
    --it-red: #d42a2a;
    --us-blue: #2a3a8c;
    --us-red: #c8262d;
    --uk-blue: #1e2a66;
  }
  * { margin: 0; padding: 0; box-sizing: border-box; }
  html, body { width: 848px; height: 1200px; overflow: hidden; background: var(--bg); }
  .poster {
    position: relative; width: 848px; height: 1200px; overflow: hidden;
    background: radial-gradient(ellipse at 50% 40%, #151515 0%, var(--bg) 70%);
    color: var(--text);
    font-family: "Pathway Gothic One", "Arial Narrow", sans-serif;
    -webkit-font-smoothing: antialiased;
  }
  .title-lettering {
    position: absolute; left: 196px; top: 18px; width: 500px; height: 165px;
    border-radius: 40px;
    background: radial-gradient(ellipse at 50% 50%, rgba(110,110,110,.35), rgba(40,40,40,0) 72%);
  }
  .branch-title {
    position: absolute; left: 0; width: 848px; top: 247px; text-align: center;
    font-size: 31px; font-weight: 400; color: #f0f0f0;
  }
  .flag { position: absolute; display: flex; }
  .flag span { flex: 1; }
  .flag--italy { left: 460px; top: 287px; width: 169px; height: 14px; }
  .flag--italy .green { background: var(--it-green); }
  .flag--italy .white { background: var(--it-white); }
  .flag--italy .red { background: var(--it-red); }
  .node {
    position: absolute; text-align: center; font-size: 13px; line-height: 17.5px; white-space: nowrap;
  }
  .flourish { position: absolute; background: var(--flourish); border-radius: 6px; }
  .flourish--top, .flourish--bottom { width: 32px; height: 5px; left: 50%; margin-left: -16px; }
  .flourish--top { top: -10px; }
  .flourish--bottom { bottom: -10px; }
  .flourish--left, .flourish--right { width: 8px; height: 26px; top: 50%; margin-top: -13px; }
  .flourish--left { left: -20px; }
  .flourish--right { right: -20px; }
  .connectors { position: absolute; left: 0; top: 0; }
  .connectors path { fill: none; stroke: var(--connector); stroke-width: 1.5; }
  .others-label { position: absolute; left: 490px; top: 940px; font-size: 29px; }
  .flag--us { left: 614px; top: 935px; width: 168px; height: 20px; flex-direction: column; }
  .flag--us span:nth-child(odd) { background: var(--us-red); }
  .flag--us span:nth-child(even) { background: #fff; }
  .flag--us .canton { position: absolute; left: 0; top: 0; width: 52px; height: 20px; background: var(--us-blue); }
  .flag--uk { left: 614px; top: 970px; width: 168px; height: 17px; background: var(--uk-blue); }
  .flag--uk .cross-h { position: absolute; left: 0; top: 6px; width: 168px; height: 5px; background: var(--us-red); }
  .flag--uk .cross-v { position: absolute; left: 80px; top: 0; width: 8px; height: 17px; background: var(--us-red); }
  .keyboard {
    position: absolute; left: 0; top: 1015px; width: 848px; height: 185px;
    background: linear-gradient(180deg, #0b0b0b 0%, #1e1e1e 22%, #cfcfcf 48%, #f2f2f2 75%, #bdbdbd 100%);
  }
</style>
</head>
<body>
<main class="poster">
  <div class="title-lettering" role="img" aria-label="Hand-lettered script title: Genealogical Trees of Pianists, over a scroll ornament"></div>

  <h2 class="branch-title">American Tree, Branch II - Italian influences</h2>
  <div class="flag flag--italy" role="img" aria-label="Italian flag"><span class="green"></span><span class="white"></span><span class="red"></span></div>

  <svg class="connectors" width="848" height="1200" aria-hidden="true">
    <path d="M270 463 H293 V793 H490"/>
    <path d="M430 588 V641 H687 V660"/>
    <path d="M687 712 V770"/>
    <path d="M687 568 V580 H764 V864 H173 V775"/>
  </svg>

  <section class="node" style="left:98px;top:384px;width:166px">
    <span class="flourish flourish--top" role="img" aria-label="ornament"></span>
    <span class="flourish flourish--left" role="img" aria-label="ornament"></span>
    <span class="flourish flourish--right" role="img" aria-label="ornament"></span>
    Edwin Harlowe<br>(1889-1970) Students:<br>Conrad Wexley (1927-2012)<br>Sidney Larkin (1927)<br>Claude Ferrand (1925-2014)<br>Abel Sorrell (1922)<br>Jorge Balanza (1914-1990)<br>Elinor Sadowska (1914)<br>Sasha Cheremin (1909-1995)
    <span class="flourish flourish--bottom" role="img" aria-label="ornament"></span>
  </section>

  <section class="node" style="left:352px;top:389px;width:156px">
    <span class="flourish flourish--top" role="img" aria-label="ornament"></span>
    <span class="flourish flourish--left" role="img" aria-label="ornament"></span>
    <span class="flourish flourish--right" role="img" aria-label="ornament"></span>
    Edmund Steinhart (1892-1964)<br>Students:<br>Joseph Kalman (1946)<br>Barak Amsel (1990)<br>Jerome Lindqvist (1932)<br>Alfred Brenner (1931)<br>Russell Shepard (1930)<br>Maura Lyndale (1916-2005)<br>Irwin Falkner (1908-1977)<br>Jakob Gerlach (1906-1989)
    <span class="flourish flourish--bottom" role="img" aria-label="ornament"></span>
  </section>

  <section class="node" style="left:606px;top:384px;width:166px">
    <span class="flourish flourish--top" role="img" aria-label="ornament"></span>
    <span class="flourish flourish--left" role="img" aria-label="ornament"></span>
    <span class="flourish flourish--right" role="img" aria-label="ornament"></span>
    Marta Corvino<br>(1889-1970) Students:<br>Conrad Wexley (1927-2012)<br>Sidney Larkin (1927)<br>Claude Ferrand (1925-2014)<br>Abel Sorrell (1922)<br>Jorge Balanza (1914-1990)<br>Elinor Sadowska (1914)<br>Sasha Cheremin (1909-1995)
    <span class="flourish flourish--bottom" role="img" aria-label="ornament"></span>
  </section>

  <section class="node" style="left:98px;top:646px;width:166px">
    <span class="flourish flourish--top" role="img" aria-label="ornament"></span>
    <span class="flourish flourish--left" role="img" aria-label="ornament"></span>
    <span class="flourish flourish--right" role="img" aria-label="ornament"></span>
    Guido Arnaldi<br>(1901-1989) Students:<br>Horacio Galvez (1948)<br>Daniel Prescott (1935)<br>Raymond Lowell (1923-1988)<br>Julian Marsh
    <span class="flourish flourish--bottom" role="img" aria-label="ornament"></span>
  </section>

  <section class="node" style="left:390px;top:663px;width:80px">
    <span class="flourish flourish--top" role="img" aria-label="ornament"></span>
    <span class="flourish flourish--left" role="img" aria-label="ornament"></span>
    <span class="flourish flourish--right" role="img" aria-label="ornament"></span>
    Carlo Zanetti<br>(1903-1984)
    <span class="flourish flourish--bottom" role="img" aria-label="ornament"></span>
  </section>
  <section class="node" style="left:520px;top:663px;width:80px">
    <span class="flourish flourish--top" role="img" aria-label="ornament"></span>
    <span class="flourish flourish--left" role="img" aria-label="ornament"></span>
    <span class="flourish flourish--right" role="img" aria-label="ornament"></span>
    Carlo Zanetti<br>(1903-1984)
    <span class="flourish flourish--bottom" role="img" aria-label="ornament"></span>
  </section>
  <section class="node" style="left:647px;top:663px;width:80px">
    <span class="flourish flourish--top" role="img" aria-label="ornament"></span>
    <span class="flourish flourish--left" role="img" aria-label="ornament"></span>
    <span class="flourish flourish--right" role="img" aria-label="ornament"></span>
    Carlo Zanetti<br>(1903-1984)
    <span class="flourish flourish--bottom" role="img" aria-label="ornament"></span>
  </section>
  <section class="node" style="left:504px;top:775px;width:80px">
    <span class="flourish flourish--top" role="img" aria-label="ornament"></span>
    <span class="flourish flourish--left" role="img" aria-label="ornament"></span>
    <span class="flourish flourish--right" role="img" aria-label="ornament"></span>
    Carlo Zanetti<br>(1903-1984)
    <span class="flourish flourish--bottom" role="img" aria-label="ornament"></span>
  </section>
  <section class="node" style="left:647px;top:775px;width:80px">
    <span class="flourish flourish--top" role="img" aria-label="ornament"></span>
    <span class="flourish flourish--left" role="img" aria-label="ornament"></span>
    <span class="flourish flourish--right" role="img" aria-label="ornament"></span>
    Carlo Zanetti<br>(1903-1984)
    <span class="flourish flourish--bottom" role="img" aria-label="ornament"></span>
  </section>

  <p class="others-label">others flags</p>
  <div class="flag flag--us" role="img" aria-label="United States flag">
    <span></span><span></span><span></span><span></span><span></span><span></span><span></span>
    <i class="canton"></i>
  </div>
  <div class="flag flag--uk" role="img" aria-label="United Kingdom flag">
    <i class="cross-h"></i><i class="cross-v"></i>
  </div>

  <div class="keyboard" role="img" aria-label="Piano keyboard in perspective"></div>
</main>
</body>
</html>
```